Business Cards for a law firm

Business cards for our law firm. Use our silhoette logo and OAK HARBOR - check our website (www.oakharbor-legal.com)

Contact Information for Business Card

our silhouette logo, OAK HARBOR, 800-555-0147, Dorian Kestrup, dorian@oakharbor-legal.com

Requirements
Must have
• our silhouette logo, OAK HARBOR, 800-555-0147, Dorian Kestrup, dorian@oakharbor-legal.com

```html
<!DOCTYPE html>
<html lang="en">
<head>
<meta charset="utf-8">
<title>Oak Harbor – Business Cards</title>
<link rel="stylesheet" href="https://fonts.googleapis.com/css2?family=Tenor+Sans&family=Arimo:wght@400&display=swap">
<style>
  :root {
    --backdrop: #9a9a9a;
    --paper: #fbfbfb;
    --navy: #1b2d69;
    --navy-soft: #2f4585;
    --ink: #3a3a3a;
    --white: #ffffff;
  }
  * { box-sizing: border-box; margin: 0; padding: 0; }
  html, body {
    width: 1200px; height: 1050px; overflow: hidden;
    background: var(--backdrop);
  }
  .stage { position: relative; width: 1200px; height: 1050px; }

  .card {
    position: absolute;
    border-radius: 22px;
    box-shadow: 0 6px 18px rgba(0,0,0,0.18);
  }

  /* Front: portrait, white */
  .card-front {
    left: 110px; top: 228px; width: 340px; height: 595px;
    background: var(--paper);
    display: flex; flex-direction: column; align-items: center;
  }
  .front-brand {
    margin-top: 150px;
    font-family: "Tenor Sans", sans-serif;
    font-size: 26px; letter-spacing: 4px;
    color: var(--navy-soft);
  }
  .holder-name {
    margin-top: 70px;
    font-family: "Tenor Sans", sans-serif;
    font-size: 26px; letter-spacing: 1px;
    font-variant: small-caps;
    color: var(--navy);
  }
  .contact-divider {
    margin-top: 18px;
    display: flex; align-items: center; gap: 6px;
  }
  .contact-divider .rule { width: 18px; height: 1px; background: var(--ink); }
  .contact-divider svg { display: block; }
  .contact-list {
    margin-top: 16px; list-style: none; text-align: center;
    font-family: "Arimo", sans-serif; font-size: 17px; line-height: 26px;
    color: var(--ink);
  }

  /* Back: landscape, navy */
  .card-back {
    left: 505px; top: 355px; width: 595px; height: 340px;
    background: var(--navy);
    border: 3px solid var(--white);
    display: flex; align-items: center; justify-content: center;
  }
  .back-brand {
    font-family: "Tenor Sans", sans-serif;
    font-size: 46px; letter-spacing: 7px;
    color: var(--white);
  }
</style>
</head>
<body>
<main class="stage">
  <section class="card card-front" aria-label="Card front">
    <div class="front-brand">OAK HARBOR</div>
    <h1 class="holder-name">Dorian Kestrup</h1>
    <div class="contact-divider">
      <span class="rule"></span>
      <svg width="78" height="24" viewBox="0 0 78 24" aria-hidden="true">
        <circle cx="12" cy="12" r="11" fill="var(--navy-soft)"/>
        <path d="M8 7 l3 0 l1 3 l-2 1 a7 7 0 0 0 3 3 l1 -2 l3 1 l0 3 a9 9 0 0 1 -9 -9z" fill="var(--white)"/>
        <circle cx="39" cy="12" r="11" fill="var(--navy-soft)"/>
        <rect x="32" y="8" width="14" height="9" fill="none" stroke="var(--white)" stroke-width="1.5"/>
        <path d="M32 8 l7 5 l7 -5" fill="none" stroke="var(--white)" stroke-width="1.5"/>
        <circle cx="66" cy="12" r="11" fill="var(--navy-soft)"/>
        <circle cx="66" cy="12" r="6" fill="none" stroke="var(--white)" stroke-width="1.5"/>
        <path d="M60 12 h12 M66 6 v12" stroke="var(--white)" stroke-width="1.2"/>
      </svg>
      <span class="rule"></span>
    </div>
    <ul class="contact-list">
      <li>800-555-0147</li>
      <li>dorian@oakharbor-legal.com</li>
      <li>www.oakharbor-legal.com</li>
    </ul>
  </section>

  <section class="card card-back" aria-label="Card back">
    <div class="back-brand">OAK HARBOR</div>
  </section>
</main>
</body>
</html>
```